SunnyPawLand Webshop and Logo Design

We need a complete design for our new Webshop
We sell pet accessories for dogs, cats, guinea pigs and some other animals
The provided logo ist a first draft for our logo and not final. you can be creative.
Maybe you can bring in some "Happyness" :o)
The Website will be a PressKit/KartMill System with a "ShopCanvas" Theme. We can provide a test environment, but it must be transferable to the final website.
In the First step, we need a finalized logo, then the WebDesign.

We need the following items.

* Company Icon
* Favicon 512*512 (from company icon)
* Shipping Label Icon (300px*100px, transparent background)
* Label Icon (600px*150px, transparent background)
* WebShop Design/Child-Theme
* Businesscard

Target Market(s)

German retail for pet accessories

Industry/Entity Type

Pet

Logo Text

SunnyPawLand

Coding

Coded - Design and coding required

Number of Pages Required

3 page

Colors

Designer to choose colors to be used in the design.

Requirements
Must have
• Cat, Dog, and Guineapig must be present
• The design must communicate happy pets.

```html
<!DOCTYPE html>
<html lang="en">
<head>
<meta charset="utf-8">
<title>SunnyPawLand – Pet Shop</title>
<link href="https://fonts.googleapis.com/css2?family=Open+Sans:wght@400;600;700;800&display=swap" rel="stylesheet">
<style>
:root{
  --navy:#0c3566;
  --blue:#1570c4;
  --blue-light:#3b93de;
  --green:#79b82a;
  --green-dark:#5f9a1c;
  --green-deep:#4c8214;
  --ink:#2c3440;
  --muted:#7a8490;
  --paper:#ffffff;
  --panel:#f1f3f5;
  --line:#dfe3e7;
}
*{box-sizing:border-box;margin:0;padding:0}
html,body{width:867px;height:1200px;overflow:hidden}
body{font-family:"Open Sans",Arial,sans-serif;color:var(--ink);background:var(--paper);position:relative}

.topbar{height:22px;background:var(--navy);color:#cfe0f2;font-size:8px;display:flex;align-items:center;justify-content:space-between;padding:0 60px}
.topbar-links{display:flex;gap:14px;align-items:center}
.topbar-cart{background:var(--green);color:#fff;padding:3px 8px;border-radius:2px;font-weight:700}

.header{height:64px;display:flex;align-items:center;padding:0 60px;gap:30px;background:var(--paper)}
.brand{display:flex;align-items:center;gap:7px;color:var(--blue);font-weight:800;font-size:18px}
.brand-dot{width:22px;height:22px;border-radius:50%;background:var(--green)}
.nav{display:flex;gap:22px;font-size:10px;font-weight:700;color:var(--ink);flex:1}
.search{width:110px;height:20px;border:1px solid var(--line);border-radius:2px;display:flex;align-items:center;justify-content:space-between;padding:0 6px;font-size:8px;color:var(--muted)}

.hero{height:189px;background:linear-gradient(90deg,var(--blue) 0%,var(--blue-light) 100%);position:relative;color:#fff}
.hero-text{position:absolute;left:60px;top:34px;width:250px}
.hero-title{font-size:27px;font-weight:800;line-height:1.1}
.hero-copy{font-size:8.5px;line-height:1.5;margin:10px 0 14px;color:#e3efff}
.btn{display:inline-block;background:var(--green);color:#fff;font-size:9px;font-weight:800;padding:7px 14px;border-radius:2px}
.hero-photo{position:absolute;right:60px;top:0;width:420px;height:189px;background:linear-gradient(120deg,#9cc6ea 0%,#d9b48a 55%,#6e5a48 100%)}

.promos{display:flex;height:187px}
.promo{flex:1;position:relative;background:var(--green);color:#fff;overflow:hidden;border-right:2px solid #fff}
.promo:last-child{border-right:none}
.promo:nth-child(2){background:var(--green-dark)}
.promo-text{position:absolute;left:18px;top:24px;right:14px;z-index:1}
.promo-title{font-size:22px;font-weight:800;line-height:1.1}
.promo-copy{font-size:7.5px;line-height:1.5;margin-top:10px;color:#eef7df;width:112px}
.promo-photo{position:absolute;right:0;bottom:0;width:140px;height:102px}
.promo:nth-child(1) .promo-photo{background:linear-gradient(135deg,#c8b39a,#8a6b4f)}
.promo:nth-child(2) .promo-photo{background:linear-gradient(135deg,#f2c53d,#3aa05a)}
.promo:nth-child(3) .promo-photo{background:linear-gradient(135deg,#efe6d6,#b89a78)}

.catalog{background:var(--panel);height:520px;padding:30px 60px 0}
.grid{display:grid;grid-template-columns:repeat(4,173px);column-gap:18px;row-gap:14px}
.card-image{height:160px;background:var(--paper);border:1px solid var(--line);display:flex;align-items:center;justify-content:center}
.card-image span{width:120px;height:110px;border-radius:6px}
.card-name{font-size:9.5px;font-weight:700;margin-top:8px}
.card-price{font-size:8px;color:var(--green-dark);font-weight:700;margin-top:2px}
.card-copy{font-size:7.5px;color:var(--muted);line-height:1.45;margin-top:3px}

.footer{position:absolute;left:0;top:982px;width:867px;height:198px;background:var(--green);color:#fff;display:flex;padding:34px 60px 0;gap:60px}
.footer-about{width:250px}
.footer-about .brand{color:#fff}
.footer-about .brand-dot{background:#fff}
.footer-about p{font-size:7.5px;line-height:1.55;margin-top:10px;color:#eef7df}
.footer-col h4{font-size:10px;font-weight:700;margin-bottom:8px}
.footer-col li{list-style:none;font-size:8px;line-height:1.9;color:#eef7df;display:flex;align-items:center;gap:6px}
.footer-col li::before{content:"";width:3px;height:3px;border-radius:50%;background:#fff}
.contacts li::before{display:none}
.contacts svg{width:10px;height:10px;fill:#fff}
.footer-categories{width:180px}
.bottombar{position:absolute;left:0;top:1180px;width:867px;height:20px;background:var(--green-deep);color:#e4f0d2;font-size:7px;display:flex;align-items:center;justify-content:space-between;padding:0 60px}
.social{display:flex;gap:5px}
.social span{width:9px;height:9px;border-radius:50%;background:#fff}
</style>
</head>
<body>

<div class="topbar">
  <span>Free shipping on all orders over $49 today</span>
  <div class="topbar-links"><span>Login</span><span>Register</span><span>Wishlist</span><span>Checkout</span><span class="topbar-cart">$0.00 Cart</span></div>
</div>

<header class="header">
  <div class="brand"><span class="brand-dot"></span>SunnyPawLand</div>
  <nav class="nav"><span>Food &amp; Treats</span><span>Accessories</span><span>Cages &amp; Aquariums</span><span>Toys</span><span>Grooming</span></nav>
  <div class="search"><span>Search</span>
    <svg width="9" height="9" viewBox="0 0 10 10"><circle cx="4" cy="4" r="3" fill="none" stroke="#7a8490" stroke-width="1.3"/><line x1="6.3" y1="6.3" x2="9" y2="9" stroke="#7a8490" stroke-width="1.3"/></svg>
  </div>
</header>

<section class="hero">
  <div class="hero-text">
    <h1 class="hero-title">Welcome to<br>SunnyPawLand</h1>
    <p class="hero-copy">Here you'll find everything you need for your best furry friend. Shop premium pet food, accessories, grooming supplies, and more!</p>
    <span class="btn">SHOP NOW</span>
  </div>
  <div class="hero-photo" role="img" aria-label="Photo of a happy boy hugging a dog, with a cat sitting beside them"></div>
</section>

<section class="promos">
  <div class="promo">
    <div class="promo-text"><h2 class="promo-title">Dog &amp; Cat<br>Treats</h2><p class="promo-copy">Tasty snacks for happy pets, picked fresh and delivered fast.</p></div>
    <div class="promo-photo" role="img" aria-label="Photo of a dog and a cat together"></div>
  </div>
  <div class="promo">
    <div class="promo-text"><h2 class="promo-title">Best Bird<br>Supplies</h2><p class="promo-copy">Seeds, perches and cages for cheerful birds of every size.</p></div>
    <div class="promo-photo" role="img" aria-label="Photo of colourful parrots on a branch"></div>
  </div>
  <div class="promo">
    <div class="promo-text"><h2 class="promo-title">Safe and Fun<br>Toys</h2><p class="promo-copy">Playful toys tested for safety, made for hours of fun.</p></div>
    <div class="promo-photo" role="img" aria-label="Photo of a rabbit beside colourful eggs"></div>
  </div>
</section>

<section class="catalog">
  <div class="grid">
    <article><div class="card-image"><span role="img" aria-label="Product photo of chew ropes with a puppy" style="background:linear-gradient(135deg,#3a3a3a,#c9a36a)"></span></div><h3 class="card-name">Chew Ropes</h3><p class="card-price">Price: $8.00</p><p class="card-copy">Durable and safe, made for daily play and care.</p></article>
    <article><div class="card-image"><span role="img" aria-label="Product photo of a travel food and water bowl" style="background:linear-gradient(135deg,#9fd24a,#4a8a1a)"></span></div><h3 class="card-name">On the Go Food and Water Bowl</h3><p class="card-price">Price: $8.00</p><p class="card-copy">Light and handy bowl for walks, trips and outings.</p></article>
    <article><div class="card-image"><span role="img" aria-label="Product photo of a dog with rubber chew toys" style="background:linear-gradient(135deg,#e7c98f,#2f6fb7)"></span></div><h3 class="card-name">Chew Rubber Toys</h3><p class="card-price">Price: $8.00</p><p class="card-copy">Durable and safe, made for daily play and care.</p></article>
    <article><div class="card-image"><span role="img" aria-label="Product photo of assorted rubber chew toys" style="background:linear-gradient(135deg,#e04a3a,#f2c23d,#3a9a4a)"></span></div><h3 class="card-name">Chew Rubber Toys</h3><p class="card-price">Price: $8.00</p><p class="card-copy">Bright, tough toys that keep teeth clean and healthy.</p></article>
    <article><div class="card-image"><span role="img" aria-label="Product photo of a small pet exercise ball" style="background:radial-gradient(circle,#b8f0d8,#5cc6a0)"></span></div><h3 class="card-name">Exercise Ball</h3><p class="card-price">Price: $8.00</p><p class="card-copy">Roll and explore safely, great for small pets.</p></article>
    <article><div class="card-image"><span role="img" aria-label="Product photo of a green bone-shaped ID tag" style="background:linear-gradient(135deg,#8fd03a,#5e9a1e)"></span></div><h3 class="card-name">Personalized ID Tag</h3><p class="card-price">Price: $8.00</p><p class="card-copy">Engraved with name and phone for peace of mind.</p></article>
    <article><div class="card-image"><span role="img" aria-label="Product photo of two small toy figures" style="background:linear-gradient(135deg,#f2b23a,#3a7ac8)"></span></div><h3 class="card-name">Metal Bird Cage</h3><p class="card-price">Price: $8.00</p><p class="card-copy">Sturdy frame with easy access and roomy space.</p></article>
    <article><div class="card-image"><span role="img" aria-label="Product photo of a white metal bird cage" style="background:linear-gradient(135deg,#eef2f6,#9fb7cf)"></span></div><h3 class="card-name">Metal Bird Cage</h3><p class="card-price">Price: $8.00</p><p class="card-copy">Sturdy frame with easy access and roomy space.</p></article>
  </div>
</section>

<footer class="footer">
  <div class="footer-about">
    <div class="brand"><span class="brand-dot"></span>SunnyPawLand</div>
    <p>Your friendly shop for pet accessories, food and toys. We bring happiness to dogs, cats, guinea pigs and birds with quality products and caring service every single day.</p>
  </div>
  <div class="footer-col footer-categories">
    <h4>Categories</h4>
    <ul><li>Food &amp; Treats</li><li>Accessories</li><li>Cages &amp; Aquariums</li><li>Toys</li><li>Grooming</li></ul>
  </div>
  <div class="footer-col contacts">
    <h4>Contacts</h4>
    <ul>
      <li><svg viewBox="0 0 10 10"><path d="M2 0.5l2 2-1 1.3c.7 1.4 1.8 2.5 3.2 3.2l1.3-1 2 2-1.2 1.5C4.5 9.2.8 5.5.5 1.7z"/></svg>+1 (555) 014-2280</li>
      <li><svg viewBox="0 0 10 10"><path d="M5 0a3.5 3.5 0 0 1 3.5 3.5C8.5 6 5 10 5 10S1.5 6 1.5 3.5A3.5 3.5 0 0 1 5 0zm0 2a1.5 1.5 0 1 0 0 3 1.5 1.5 0 0 0 0-3z"/></svg>48 Meadow Lane, Brightfield</li>
      <li><svg viewBox="0 0 10 10"><path d="M0 2h10v6H0zM0.5 2.3L5 5.6 9.5 2.3" stroke="#79b82a" stroke-width="0.8"/></svg>hello@sunnypawland.example</li>
    </ul>
  </div>
</footer>
<div class="bottombar">
  <span>© SunnyPawLand 2024. All rights reserved.</span>
  <div class="social"><span></span><span></span><span></span></div>
</div>

</body>
</html>
```